Graphic Design for Hydration/ Water Bottle Brand

Spell out "Kulot" using our hydration bottles (attached).
Each letter will consist of a different color.
M- 4 bottles
A- 3 bottles
Y- 3 bottles
I- 3 bottles
M- 4 bottles

Hydration/ Water Bottles

```html
<!DOCTYPE html>
<html lang="en">
<head>
<meta charset="utf-8">
<title>Kulot Hydration Bottles Poster</title>
<link rel="stylesheet" href="https://fonts.googleapis.com/css2?family=Montserrat:wght@800;900&display=swap">
<style>
  :root {
    --backdrop: #555555;
    --navy-deep: #0d2544;
    --navy-mid: #1b3a63;
    --aqua-light: #bfeaf7;
    --aqua-mid: #5cc6ea;
    --aqua-deep: #2a9fd6;
    --card: #f3f3f3;
    --tile-dark: #0c2a5c;
    --tile-bright: #1a5fc0;
    --rule: #1f5fae;
    --white: #ffffff;
    --pink: #ec8aa6;
    --black: #111111;
    --green: #6cc58a;
    --red: #e02a1e;
    --yellow: #f3d22a;
    --magenta: #e33588;
    --lavender: #a9b5e6;
    --blue: #0b3ea0;
  }
  * { margin: 0; padding: 0; box-sizing: border-box; }
  html, body { width: 1200px; height: 1000px; overflow: hidden; }
  body { background: var(--backdrop); position: relative; font-family: "Montserrat", sans-serif; }

  .poster {
    position: absolute; left: 272px; top: 75px; width: 658px; height: 850px;
    overflow: hidden;
  }
  .poster__water-top {
    position: absolute; left: 0; top: 0; width: 100%; height: 432px;
    background: radial-gradient(ellipse at 40% 40%, var(--navy-mid), var(--navy-deep) 75%);
  }
  .poster__water-bottom {
    position: absolute; left: 0; top: 432px; width: 100%; height: 418px;
    background: radial-gradient(ellipse at 30% 90%, var(--aqua-light), var(--aqua-mid) 55%, var(--aqua-deep));
  }
  .poster__title {
    position: absolute; left: 0; top: 38px; width: 100%;
    text-align: center; color: var(--white);
    font-weight: 900; font-size: 142px; line-height: 1; letter-spacing: 2px;
  }
  .letter-card {
    position: absolute; left: 40px; top: 151px; width: 576px; height: 659px;
    background: var(--card); border-radius: 16px;
    box-shadow: 0 4px 18px rgba(0,0,0,.25);
  }
  .letter-row { position: absolute; left: 34px; width: 514px; height: 127px; }
  .letter-row + .letter-row::before { content: ""; }
  .letter-row__rule {
    position: absolute; left: 34px; width: 514px; height: 2px; background: var(--rule);
  }
  .letter-tile {
    position: absolute; left: 0; top: 0; width: 112px; height: 112px; border-radius: 12px;
    background: linear-gradient(90deg, var(--tile-dark), var(--tile-bright) 50%, var(--tile-dark));
    color: var(--white); font-weight: 800; font-size: 80px;
    display: flex; align-items: center; justify-content: center;
  }
  .bottle {
    position: absolute; top: 8px; width: 34px; height: 100px; border-radius: 6px;
  }
  .bottle::before {
    content: ""; position: absolute; left: 6px; top: 0; width: 22px; height: 16px;
    background: rgba(255,255,255,.6); border-radius: 3px;
  }
  .b1 { left: 176px; } .b2 { left: 254px; } .b3 { left: 334px; } .b4 { left: 417px; }
  .pink { background: var(--pink); } .black { background: var(--black); }
  .green { background: var(--green); } .red { background: var(--red); }
  .yellow { background: var(--yellow); } .magenta { background: var(--magenta); }
  .lavender { background: var(--lavender); } .blue { background: var(--blue); }
</style>
</head>
<body>
  <main class="poster">
    <div class="poster__water-top" role="img" aria-label="Dark blue rippling water surface"></div>
    <div class="poster__water-bottom" role="img" aria-label="Light blue swirling water with bubbles"></div>
    <h1 class="poster__title">KULOT</h1>

    <section class="letter-card">
      <div class="letter-row" style="top:17px">
        <div class="letter-tile">K</div>
        <div class="bottle b1 pink" role="img" aria-label="Pink sleeved water bottle"></div>
        <div class="bottle b2 black" role="img" aria-label="Black sleeved water bottle"></div>
        <div class="bottle b3 green" role="img" aria-label="Green sleeved water bottle"></div>
        <div class="bottle b4 red" role="img" aria-label="Red sleeved water bottle"></div>
      </div>
      <div class="letter-row__rule" style="top:136px"></div>

      <div class="letter-row" style="top:145px">
        <div class="letter-tile">U</div>
        <div class="bottle b1 yellow" role="img" aria-label="Yellow sleeved water bottle"></div>
        <div class="bottle b2 magenta" role="img" aria-label="Magenta sleeved water bottle"></div>
        <div class="bottle b3 lavender" role="img" aria-label="Lavender sleeved water bottle"></div>
      </div>
      <div class="letter-row__rule" style="top:263px"></div>

      <div class="letter-row" style="top:272px">
        <div class="letter-tile">L</div>
        <div class="bottle b1 blue" role="img" aria-label="Blue sleeved water bottle"></div>
        <div class="bottle b2 black" role="img" aria-label="Black sleeved water bottle"></div>
        <div class="bottle b3 yellow" role="img" aria-label="Yellow sleeved water bottle"></div>
      </div>
      <div class="letter-row__rule" style="top:390px"></div>

      <div class="letter-row" style="top:399px">
        <div class="letter-tile">O</div>
        <div class="bottle b1 pink" role="img" aria-label="Pink sleeved water bottle"></div>
        <div class="bottle b2 magenta" role="img" aria-label="Magenta sleeved water bottle"></div>
        <div class="bottle b3 red" role="img" aria-label="Red sleeved water bottle"></div>
      </div>
      <div class="letter-row__rule" style="top:517px"></div>

      <div class="letter-row" style="top:526px">
        <div class="letter-tile">T</div>
        <div class="bottle b1 yellow" role="img" aria-label="Yellow sleeved water bottle"></div>
        <div class="bottle b2 green" role="img" aria-label="Green sleeved water bottle"></div>
        <div class="bottle b3 blue" role="img" aria-label="Blue sleeved water bottle"></div>
        <div class="bottle b4 lavender" role="img" aria-label="Lavender sleeved water bottle"></div>
      </div>
    </section>
  </main>
</body>
</html>
```